Web portal for events

The project is about creating a web application - portal for culture events in Denmark.

Design

We aim for very simplistic, light and fully responsive design. The white background is preferable, as well as light color tones. As inspirational points we like the colors used in www.brimvale.com and www.tallowpine.org

FORMAT AND REQUIREMENTS:
1. Design should be provided based on the wireframes specified as a link below.
2. The design (and all of its pages) should be provided in three resolution variants:
- Desktop
- Tablet
- Phone
3. The design should be provided as PSD, where each page/section should be in its own PSD file
4. All graphical elements in the design should be delivered as single layers which can then be extracted from the PSD.
5. All graphical elements (icons, graphical buttons, etc.) should be provided as vector objects in the PSD, so that they can be exported into different sizes without loss of quality (for responsiveness)
6. The design should use either web safe fonts or Google Fonts.

RESPONSIVENESS
The web application should be visible on any devices (i.e. responsive design)

WIREFRAMES:
https://quillmarsh.examplewire.com/projects/eventloom/prototype/Homepage?key=0000000000000000000000000000000000000000

We expect design of the following wireframes:

Homepage:
https://quillmarsh.examplewire.com/projects/eventloom/Homepage

For arrangører - billede uploaded:
https://quillmarsh.examplewire.com/projects/eventloom/For%20arrang%C3%B8rer%20-%20billede%20uploaded

Further specifications of the project (i.e. functionality, etc.):
https://files.dorvexa.com/document/d/0AbCdEfGhIjKlMnOpQrStUvWxYz0123456789abcdefg/edit?usp=sharing
Updates

```html
<!DOCTYPE html>
<html lang="da">
<head>
<meta charset="utf-8">
<title>VIBRA – din guide til kultur og events</title>
<link href="https://fonts.googleapis.com/css2?family=Arimo:ital,wght@0,400;0,700;1,400&display=swap" rel="stylesheet">
<style>
:root{
  --navy:#1f2550;
  --navy-deep:#171c42;
  --nav:#2b3160;
  --orange:#d9560f;
  --ink:#1f2550;
  --text:#666a7a;
  --muted:#9a9a9a;
  --line:#e3e3e3;
  --grey-btn:#c9c9c9;
  --footer:#e6e6e8;
}
*{box-sizing:border-box;margin:0;padding:0}
html,body{width:934px;height:1200px;overflow:hidden;background:#fff}
body{font-family:"Arimo",Arial,sans-serif;color:var(--ink);position:relative}
.abs{position:absolute}

/* header */
.site-header{position:absolute;left:0;top:0;width:934px;height:98px;background:var(--navy)}
.brand{left:97px;top:10px;color:#fff;font-size:46px;font-weight:400;letter-spacing:2px;line-height:52px}
.tagline{left:97px;top:66px;color:#fff;font-size:9px;font-weight:700}
.account{top:17px;display:flex;gap:6px;align-items:center;color:#fff;font-size:11.5px;font-weight:700}
.search{left:502px;top:52px;width:197px;height:28px;display:flex}
.search-field{flex:1;background:#3a4068;color:#9ea3bd;font-size:11px;padding:8px 10px}
.search-btn{width:29px;background:var(--navy-deep);display:flex;align-items:center;justify-content:center}
.adv-btn{left:705px;top:52px;width:132px;height:28px;background:var(--orange);color:#fff;font-size:11.5px;font-weight:700;text-align:center;line-height:28px}

/* nav */
.main-nav{position:absolute;left:0;top:98px;width:934px;height:46px;background:var(--nav);display:flex;padding-left:97px}
.main-nav a{color:#c9cce0;font-size:13.5px;text-decoration:none;line-height:46px;padding:0 17px;border-right:1px solid #1f2550}
.main-nav a.active{background:var(--orange);color:#fff}

/* hero */
.hero{position:absolute;left:0;top:144px;width:934px;height:370px;
  background:radial-gradient(ellipse at 72% 40%,#6a3a7a 0%,#3a2d6a 40%,#1f2458 75%),#1f2458}
.hero-kicker{left:97px;top:214px;color:#dfe0ee;font-size:19px;letter-spacing:.3px}
.hero-title{left:96px;top:245px;color:var(--orange);font-size:38px;font-weight:700}
.hero-date{left:98px;top:308px;color:#fff;font-size:30px}
.hero-rule{left:97px;top:347px;width:190px;height:3px;background:#5c6088}
.hero-copy{left:97px;top:360px;width:350px;color:#d4d6e6;font-size:11.5px;line-height:18px}
.hero-cta{left:98px;top:430px;width:126px;height:39px;background:var(--orange);color:#fff;font-size:12.5px;font-weight:700;text-align:center;line-height:39px}

/* events */
.section-title{font-size:17px;font-weight:700;color:var(--ink);letter-spacing:.2px}
.title-rule{height:3px;background:#cfcfd4}
.sorter{left:350px;top:535px;display:flex;align-items:center;gap:4px;font-size:12px}
.sorter .label{font-weight:700;margin-right:2px}
.chip{height:20px;border:1px solid #c8c8c8;font-size:10px;color:#666;padding:0 8px;line-height:18px;background:#fff}
.chip.active{background:var(--orange);border-color:var(--orange);color:#fff}
.chip.select{padding-right:0;display:flex}
.chip.select span.arrow{width:16px;background:#ddd;margin-left:8px;display:flex;align-items:center;justify-content:center}

.event-card{position:absolute;width:163px}
.event-photo{width:163px;height:84px;position:relative}
.date-badge{position:absolute;left:4px;bottom:0;width:30px;height:38px;background:var(--navy);color:#fff;text-align:center;padding-top:4px}
.date-badge b{display:block;font-size:14px;font-style:italic;line-height:14px}
.date-badge small{font-size:9px}
.event-name{margin-top:11px;font-size:12.5px;font-weight:700;color:var(--ink)}
.event-desc{margin-top:6px;font-size:10px;line-height:15px;color:var(--text)}
.event-foot{margin-top:10px;display:flex;justify-content:space-between;align-items:center;width:137px}
.see-btn{width:54px;height:16px;background:var(--grey-btn);color:#666;font-size:9px;text-align:center;line-height:16px}
.see-btn.primary{background:var(--navy);color:#fff}
.likes{display:flex;align-items:center;gap:3px;font-size:11px;color:#777}

.divider{left:641px;top:535px;width:1px;height:593px;background:var(--line)}

/* favourites */
.fav{position:absolute;left:660px;width:177px;height:73px;border-bottom:1px solid var(--line);display:flex;gap:9px}
.fav-photo{width:78px;height:50px;flex:none}
.fav-name{font-size:11.5px;line-height:13.5px;color:var(--ink);margin-top:2px}
.fav-name.hot{color:var(--orange)}
.fav-date{font-size:9.5px;font-weight:700;color:var(--muted);margin-top:5px}

/* newsletter */
.newsletter{left:660px;top:958px;width:177px;height:170px;border:1px solid #d6d6d6}
.nl-head{height:38px;border-bottom:1px solid #d6d6d6;display:flex;align-items:center;gap:8px;padding-left:14px;font-size:15px;font-weight:700}
.nl-copy{padding:10px 16px 0;font-size:9px;font-style:italic;line-height:17.5px;color:var(--muted)}
.nl-form{position:absolute;left:14px;top:133px;width:148px;height:22px;border:1px solid var(--navy);display:flex}
.nl-form span{flex:1;font-size:9.5px;font-style:italic;color:#999;padding:5px 8px}
.nl-form i{width:21px;background:var(--navy);display:flex;align-items:center;justify-content:center}
.airmail{position:absolute;left:-1px;bottom:-1px;width:177px;height:4px;
  background:repeating-linear-gradient(135deg,#d9560f 0 6px,#fff 6px 9px,#3a6fb3 9px 15px,#fff 15px 18px)}

/* footer */
.site-footer{position:absolute;left:0;top:1157px;width:934px;height:43px;background:var(--footer);font-size:10.5px;color:#777}
.crumbs{position:absolute;left:98px;top:15px}
.crumbs b{font-weight:400;color:#222}
.crumbs em{font-style:normal;margin:0 6px}
.copyright{position:absolute;right:97px;top:15px}
</style>
</head>
<body>

<header class="site-header">
  <div class="abs brand">VIBRA</div>
  <div class="abs tagline">DIN GUIDE TIL KULTUR OG EVENTS</div>
  <div class="abs account" style="left:697px">
    <svg width="12" height="16" viewBox="0 0 12 16"><rect x="1.5" y="7" width="9" height="8" rx="1.5" fill="none" stroke="#d9560f" stroke-width="1.6"/><path d="M3.5 7V4.5a2.5 2.5 0 0 1 5 0" fill="none" stroke="#d9560f" stroke-width="1.6"/></svg>LOGIN
  </div>
  <div class="abs account" style="left:770px">
    <svg width="16" height="15" viewBox="0 0 16 15"><circle cx="8" cy="5" r="3.5" fill="none" stroke="#d9560f" stroke-width="1.5"/><path d="M1.5 14c0-3.5 3-5.5 6.5-5.5s6.5 2 6.5 5.5z" fill="none" stroke="#d9560f" stroke-width="1.5"/></svg>SIGN UP
  </div>
  <div class="abs search"><div class="search-field">Search</div>
    <div class="search-btn"><svg width="15" height="15" viewBox="0 0 15 15"><circle cx="6" cy="6" r="4.5" fill="none" stroke="#fff" stroke-width="2"/><path d="M9.5 9.5l4 4" stroke="#fff" stroke-width="2.2"/></svg></div></div>
  <div class="abs adv-btn">ADVANCE SEARCH</div>
</header>

<nav class="main-nav">
  <a class="active">ALLE</a><a>MUSIK</a><a>SPORT</a><a>TEATER</a><a>UDSTILLING</a><a>ELDER</a><a>BORN</a><a>MOTIN</a><a style="border:none">DIVERSE</a>
</nav>

<section class="hero" role="img" aria-label="DJ mixing at turntables under purple stage light"></section>
<div class="abs hero-kicker">VIBRA IN INFORMATION MUSIC</div>
<div class="abs hero-title">MUSIC EVENTS</div>
<div class="abs hero-date">AUGUST 17-19-2014</div>
<div class="abs hero-rule"></div>
<p class="abs hero-copy">Lorem ipsum dolor sit amet, consectetur adipiscing elit. Nulla vitae cibus erat, in semper arcu. Fusce sed porta felis, eu laoreet dui. metus. Phasellus tempus molestie ipsum eget</p>
<div class="abs hero-cta">REGISTER NOW</div>

<h2 class="abs section-title" style="left:97px;top:537px">POPULER EVENTS</h2>
<div class="abs title-rule" style="left:97px;top:559px;width:115px"></div>
<div class="abs sorter">
  <span class="label">Sorter Efter</span>
  <span class="chip active">Populer</span>
  <span class="chip select">Omrade<span class="arrow"><svg width="7" height="4"><path d="M0 0h7L3.5 4z" fill="#888"/></svg></span></span>
  <span class="chip" style="margin-left:5px">Dato</span>
  <span class="chip">Pris</span>
</div>

<!-- row 1 -->
<article class="event-card" style="left:97px;top:582px">
  <div class="event-photo" role="img" aria-label="Business people reviewing documents" style="background:linear-gradient(135deg,#e8e6e2,#9a948c 60%,#3c3a40)"><div class="date-badge"><b>02</b><small>Aug</small></div></div>
  <h3 class="event-name">Jens Holmvig Koncert</h3>
  <p class="event-desc">Lorem ipsum dolor sit consectetur adipiscing lorem ispum.</p>
  <div class="event-foot"><span class="see-btn primary">Se Event</span><span class="likes"><svg width="13" height="11" viewBox="0 0 13 11"><path d="M6.5 11L1 5.5A3 3 0 0 1 6.5 1.5 3 3 0 0 1 12 5.5z" fill="#d9560f"/></svg>03</span></div>
</article>
<article class="event-card" style="left:278px;top:582px">
  <div class="event-photo" role="img" aria-label="Girls singing into a microphone" style="background:linear-gradient(135deg,#d8cfc6,#b49a8c 55%,#6a4a70)"><div class="date-badge"><b>02</b><small>Aug</small></div></div>
  <h3 class="event-name">Jens Holmvig Koncert</h3>
  <p class="event-desc">Lorem ipsum dolor sit consectetur adipiscing lorem ispum.</p>
  <div class="event-foot"><span class="see-btn">Se Event</span><span class="likes"><svg width="13" height="11" viewBox="0 0 13 11"><path d="M6.5 11L1 5.5A3 3 0 0 1 6.5 1.5 3 3 0 0 1 12 5.5z" fill="#c2c2c2"/></svg>03</span></div>
</article>
<article class="event-card" style="left:460px;top:582px">
  <div class="event-photo" role="img" aria-label="Classroom with raised hands" style="background:linear-gradient(135deg,#eef0f2,#b8bcc4 55%,#4a5060)"><div class="date-badge"><b>02</b><small>Aug</small></div></div>
  <h3 class="event-name">Jens Holmvig Koncert</h3>
  <p class="event-desc">Lorem ipsum dolor sit consectetur adipiscing lorem ispum.</p>
  <div class="event-foot"><span class="see-btn">Se Event</span><span class="likes"><svg width="13" height="11" viewBox="0 0 13 11"><path d="M6.5 11L1 5.5A3 3 0 0 1 6.5 1.5 3 3 0 0 1 12 5.5z" fill="#c2c2c2"/></svg>03</span></div>
</article>

<!-- row 2 -->
<article class="event-card" style="left:97px;top:771px">
  <div class="event-photo" role="img" aria-label="Friends laughing at a party" style="background:linear-gradient(135deg,#c2363a,#e0a070 50%,#5a2030)"><div class="date-badge"><b>02</b><small>Aug</small></div></div>
  <h3 class="event-name">Jens Holmvig Koncert</h3>
  <p class="event-desc">Lorem ipsum dolor sit consectetur adipiscing lorem ispum.</p>
  <div class="event-foot"><span class="see-btn">Se Event</span><span class="likes"><svg width="13" height="11" viewBox="0 0 13 11"><path d="M6.5 11L1 5.5A3 3 0 0 1 6.5 1.5 3 3 0 0 1 12 5.5z" fill="#c2c2c2"/></svg>03</span></div>
</article>
<article class="event-card" style="left:278px;top:771px">
  <div class="event-photo" role="img" aria-label="Fashion runway with audience" style="background:linear-gradient(135deg,#5a5a5a,#2a2a2e 50%,#8a7a70)"><div class="date-badge"><b>02</b><small>Aug</small></div></div>
  <h3 class="event-name">Jens Holmvig Koncert</h3>
  <p class="event-desc">Lorem ipsum dolor sit consectetur adipiscing lorem ispum.</p>
  <div class="event-foot"><span class="see-btn">Se Event</span><span class="likes"><svg width="13" height="11" viewBox="0 0 13 11"><path d="M6.5 11L1 5.5A3 3 0 0 1 6.5 1.5 3 3 0 0 1 12 5.5z" fill="#c2c2c2"/></svg>03</span></div>
</article>
<article class="event-card" style="left:460px;top:771px">
  <div class="event-photo" role="img" aria-label="Speaker presenting at a podium" style="background:linear-gradient(135deg,#f0f2f4,#c8ccd2 60%,#2c3448)"><div class="date-badge"><b>02</b><small>Aug</small></div></div>
  <h3 class="event-name">Jens Holmvig Koncert</h3>
  <p class="event-desc">Lorem ipsum dolor sit consectetur adipiscing lorem ispum.</p>
  <div class="event-foot"><span class="see-btn">Se Event</span><span class="likes"><svg width="13" height="11" viewBox="0 0 13 11"><path d="M6.5 11L1 5.5A3 3 0 0 1 6.5 1.5 3 3 0 0 1 12 5.5z" fill="#c2c2c2"/></svg>03</span></div>
</article>

<!-- row 3 -->
<article class="event-card" style="left:97px;top:962px">
  <div class="event-photo" role="img" aria-label="Busy shopping street with crowds" style="background:linear-gradient(135deg,#4a6a9a,#8a7a6a 50%,#3a3030)"><div class="date-badge"><b>02</b><small>Aug</small></div></div>
  <h3 class="event-name">Jens Holmvig Koncert</h3>
  <p class="event-desc">Lorem ipsum dolor sit consectetur adipiscing lorem ispum.</p>
  <div class="event-foot"><span class="see-btn">Se Event</span><span class="likes"><svg width="13" height="11" viewBox="0 0 13 11"><path d="M6.5 11L1 5.5A3 3 0 0 1 6.5 1.5 3 3 0 0 1 12 5.5z" fill="#c2c2c2"/></svg>03</span></div>
</article>
<article class="event-card" style="left:278px;top:962px">
  <div class="event-photo" role="img" aria-label="Friends celebrating together" style="background:linear-gradient(135deg,#3a4a80,#c89a70 50%,#5a4030)"><div class="date-badge"><b>02</b><small>Aug</small></div></div>
  <h3 class="event-name">Jens Holmvig Koncert</h3>
  <p class="event-desc">Lorem ipsum dolor sit consectetur adipiscing lorem ispum.</p>
  <div class="event-foot"><span class="see-btn">Se Event</span><span class="likes"><svg width="13" height="11" viewBox="0 0 13 11"><path d="M6.5 11L1 5.5A3 3 0 0 1 6.5 1.5 3 3 0 0 1 12 5.5z" fill="#c2c2c2"/></svg>03</span></div>
</article>
<article class="event-card" style="left:460px;top:962px">
  <div class="event-photo" role="img" aria-label="Nightclub bar with colourful lights" style="background:linear-gradient(135deg,#2a3aa0,#6a3a8a 50%,#1a1a50)"><div class="date-badge"><b>02</b><small>Aug</small></div></div>
  <h3 class="event-name">Jens Holmvig Koncert</h3>
  <p class="event-desc">Lorem ipsum dolor sit consectetur adipiscing lorem ispum.</p>
  <div class="event-foot"><span class="see-btn">Se Event</span><span class="likes"><svg width="13" height="11" viewBox="0 0 13 11"><path d="M6.5 11L1 5.5A3 3 0 0 1 6.5 1.5 3 3 0 0 1 12 5.5z" fill="#c2c2c2"/></svg>03</span></div>
</article>

<div class="abs divider"></div>

<!-- favourites -->
<h2 class="abs section-title" style="left:660px;top:537px">MINE FAVORITTER</h2>
<div class="abs title-rule" style="left:660px;top:559px;width:115px"></div>

<div class="fav" style="top:578px">
  <div class="fav-photo" role="img" aria-label="Friends laughing at a party" style="background:linear-gradient(135deg,#c2363a,#e0a070 50%,#5a2030)"></div>
  <div><div class="fav-name hot">Jens Holmvig Koncert</div><div class="fav-date">02 - Aug - 2014</div></div>
</div>
<div class="fav" style="top:651px">
  <div class="fav-photo" role="img" aria-label="Fashion runway" style="background:linear-gradient(135deg,#5a5a5a,#2a2a2e 50%,#8a7a70)"></div>
  <div><div class="fav-name">Lorem ipsum dolor sit amet,</div><div class="fav-date">02 - Aug - 2014</div></div>
</div>
<div class="fav" style="top:724px">
  <div class="fav-photo" role="img" aria-label="Speaker at a podium" style="background:linear-gradient(135deg,#f0f2f4,#c8ccd2 60%,#2c3448)"></div>
  <div><div class="fav-name">Jens Holmvig Koncert</div><div class="fav-date">02 - Aug - 2014</div></div>
</div>
<div class="fav" style="top:797px">
  <div class="fav-photo" role="img" aria-label="Nightclub bar with lights" style="background:linear-gradient(135deg,#2a3aa0,#6a3a8a 50%,#1a1a50)"></div>
  <div><div class="fav-name">Jens Holmvig Koncert</div><div class="fav-date">02 - Aug - 2014</div></div>
</div>
<div class="fav" style="top:870px;border:none">
  <div class="fav-photo" role="img" aria-label="Silhouettes dancing at sunset" style="background:linear-gradient(135deg,#f0a030,#c05a10 55%,#201008)"></div>
  <div><div class="fav-name">Jens Holmvig Koncert</div><div class="fav-date">02 - Aug - 2014</div></div>
</div>

<aside class="abs newsletter">
  <div class="nl-head"><svg width="20" height="18" viewBox="0 0 20 18"><path d="M1 7l9-6 9 6v10H1z" fill="none" stroke="#1f2550" stroke-width="1.6"/><path d="M1 7l9 6 9-6" fill="none" stroke="#1f2550" stroke-width="1.6"/></svg>NYHRDSBREV</div>
  <p class="nl-copy">Lorem ipsum dolor sit amet, etur adipiscing elit. Nunc laoreet etus non tortor varius, et rhon magna posuere.</p>
  <div class="nl-form"><span>Email</span><i><svg width="9" height="10"><path d="M0 0l9 5-9 5 2-5z" fill="#fff"/></svg></i></div>
  <div class="airmail"></div>
</aside>

<footer class="site-footer">
  <div class="crumbs"><b>Alle</b><em>/</em>Musik<em>/</em>Sport<em>/</em>Teater<em>/</em>Udstilling<em>/</em>Elder<em>/</em>Born<em>/</em>Motin<em>/</em>Diverse</div>
  <div class="copyright">© 2014, VIBRA. All rights reserved</div>
</footer>

</body>
</html>
```